POOL BUILDING CONTRACTOR

our company has shifter focus over the past 18 month we no longer have a retail store and no longer clean pools we build concrete pools. our website if 5 years old we need a completely new site that shows our core product, building concrete pools & renovate concrete pools

here is a few of our competitors;
brantelwaters.com
okvimbuilders.com
ridgeviewlagoonworks.com
plunvora.com
halvertonbasinsandtubs.com
dremblewaterne.com

one we land on a final design I will upload customer before and after photos and any other content needed

Target Market(s)

People looking to build or renovate there pool

Industry/Entity Type

swimming pool

Coding

Coded - Design and coding required

Number of Pages Required

5+ page

Colors
0054AA
0677BA
7BADD7
CADEEF
E8F1F8

Requirements
Must have
• financing Service-Repairs & liners new build-photos renovate-remodeling design-consult customer-reviews Gallery Before-After Contact us 3D Design & Modeling construction process & Timeline Equipment Features Hardscapes I like these sites https://meadowlarkbasinsbycraft.com/ https://holtbergwaters.com/

```html
<!DOCTYPE html>
<html lang="en">
<head>
<meta charset="utf-8">
<title>Aquavell – The Pool Service Company</title>
<link href="https://fonts.googleapis.com/css2?family=Poppins:wght@400;500;600;700&display=swap" rel="stylesheet">
<style>
:root{
  --navy:#0b2fa6;
  --royal:#1446c8;
  --bright:#1159ea;
  --sky:#c4e8f3;
  --sky-soft:#d5eef7;
  --label:#7bb3d8;
  --mist:#eff3f5;
  --text-grey:#6b7280;
  --white:#ffffff;
  --ink:#111111;
  --cyan:#52f0f7;
  --footer:#0c2f9e;
}
*{box-sizing:border-box;margin:0;padding:0}
html,body{width:1200px;height:2572px;overflow:hidden;background:var(--white);font-family:'Poppins',sans-serif}
.page{position:relative;width:1200px;height:2572px}
.abs{position:absolute}

/* header */
.site-header{left:0;top:0;width:1200px;height:88px;background:var(--white)}
.brand{display:flex;align-items:center;gap:8px}
.brand-mark{width:56px;height:56px;border:3px solid var(--royal);background:var(--sky)}
.brand-text{display:flex;flex-direction:column;color:var(--royal);font-weight:700;line-height:1}
.brand-name{font-size:44px;letter-spacing:-1px}
.brand-tag{font-size:10px;letter-spacing:.5px;margin-top:2px}
.site-header .brand{position:absolute;left:60px;top:16px}
.main-nav{position:absolute;left:448px;top:29px;display:flex;gap:12px;font-size:13px;color:var(--royal);align-items:center}
.main-nav .phone{margin-left:14px;display:flex;gap:8px;align-items:center}

/* hero */
.hero{left:0;top:88px;width:1200px;height:310px}
.hero-water{position:absolute;inset:0;background:radial-gradient(circle at 30% 40%,#4fc6ff 0,#1a66e6 40%,#0f3fc4 80%)}
.hero-title{position:absolute;top:36px;width:1185px;text-align:center;color:var(--white);font-size:30px;font-weight:500}
.hero-cta{position:absolute;left:483px;top:90px;width:220px;height:33px;border-radius:17px;background:var(--sky);color:var(--royal);font-size:17px;text-align:center;line-height:33px}

/* sections */
.band{left:0;width:1200px;background:var(--mist)}
.cols{position:absolute;left:53px;width:1094px;display:flex;gap:27px}
.col{width:346px;text-align:center;position:relative}
.copy{font-size:13px;line-height:20px;color:var(--text-grey)}
.btn{display:inline-block;width:220px;height:27px;border-radius:14px;background:var(--navy);color:var(--white);font-size:17px;font-weight:500;line-height:27px;text-align:center}
.photo{display:block;margin:0 auto}

.dream-title{position:absolute;left:53px;top:33px;width:1094px;height:35px;background:var(--sky);text-align:center;color:var(--royal);font-size:30px;font-weight:500;line-height:37px}
.dream-sub{position:absolute;left:53px;top:77px;font-size:12.5px;font-weight:600;color:var(--label)}
.style-label{margin:10px 0 8px;height:25px;background:var(--sky-soft);color:var(--label);font-size:21px;font-weight:500;line-height:27px}

.section-title{position:absolute;left:0;width:1200px;text-align:center;font-size:32px;font-weight:500;color:var(--royal)}
.section-sub{position:absolute;left:0;width:1200px;text-align:center;font-size:22px;color:var(--royal)}
.icon-box{height:107px;background:var(--white);display:flex;align-items:center;justify-content:center}
.service-name{font-size:22px;font-weight:500;color:var(--royal);margin:9px 0 6px}
.project-name{font-size:22px;font-weight:600;color:var(--ink);margin:8px 0 6px}

/* contact */
.contact-brand{left:40px;top:2032px;width:560px;height:340px;background:var(--sky);display:flex;align-items:center;justify-content:center}
.contact-form{left:613px;top:2044px;width:534px;color:var(--royal);font-size:13px}
.field-label{display:block;margin-bottom:6px}
.field{width:534px;height:31px;border:1px solid var(--royal);border-radius:3px;background:var(--white);font:13px 'Poppins',sans-serif;color:var(--text-grey);padding:0 5px;margin-bottom:18px;display:flex;align-items:center}
.field.select{color:var(--ink);justify-content:space-between}
.field.area{height:90px;align-items:flex-start;padding-top:6px}
.submit{position:absolute;left:156px;top:294px;width:222px;height:34px;border-radius:10px;background:var(--bright);color:var(--white);font-size:17px;font-weight:500;text-align:center;line-height:34px}

/* footer */
.site-footer{left:0;top:2400px;width:1200px;height:172px;background:var(--footer);color:var(--white)}
.site-footer .brand{position:absolute;left:178px;top:53px}
.site-footer .brand-mark{width:46px;height:46px;border-color:var(--white)}
.site-footer .brand-text{color:var(--white)}
.site-footer .brand-name{font-size:38px}
.footer-col{position:absolute;top:24px;font-size:13px;line-height:21px;color:#9cc0ff}
.footer-col h4{color:var(--white);font-size:13px;font-weight:600}
.footer-col .line{display:flex;gap:8px;align-items:center}
.socials{position:absolute;left:985px;top:53px;display:flex;gap:14px}
.socials span{width:32px;height:32px;border-radius:50%;background:var(--white)}
.copyright{position:absolute;top:136px;width:1200px;text-align:center;font-size:12px;font-weight:700}
</style>
</head>
<body>
<div class="page">

<header class="site-header abs">
  <div class="brand"><span class="brand-mark"></span><div class="brand-text"><span class="brand-name">Aquavell</span><span class="brand-tag">THE POOL SERVICE COMPANY</span></div></div>
  <nav class="main-nav">
    <span>Home page</span><span>About Us</span><span>Our Services</span>
    <span>Contact <svg width="12" height="10" viewBox="0 0 12 10"><rect x="0.5" y="0.5" width="11" height="9" fill="none" stroke="currentColor"/><path d="M0.5 0.5 6 5.5 11.5 0.5" fill="none" stroke="currentColor"/></svg></span>
    <span class="phone"><svg width="13" height="13" viewBox="0 0 24 24"><path fill="currentColor" d="M6.6 10.8a15 15 0 0 0 6.6 6.6l2.2-2.2a1 1 0 0 1 1-.25 11 11 0 0 0 3.6.6 1 1 0 0 1 1 1V20a1 1 0 0 1-1 1A17 17 0 0 1 3 4a1 1 0 0 1 1-1h3.5a1 1 0 0 1 1 1c0 1.25.2 2.45.6 3.6a1 1 0 0 1-.25 1z"/></svg>321 555 777</span>
  </nav>
</header>

<section class="hero abs">
  <div class="hero-water" role="img" aria-label="Sparkling blue pool water surface"></div>
  <svg class="abs" style="left:0;top:0" width="1200" height="310" viewBox="0 0 1200 310">
    <path d="M0 262 C250 170 420 250 600 240 C800 230 1000 220 1190 120 L1190 310 L0 310 Z" fill="var(--cyan)"/>
    <path d="M0 262 C250 170 420 250 600 240 C800 230 1000 220 1190 120 L1190 310 L0 310 Z" fill="var(--cyan)"/>
    <path d="M0 355 C200 230 450 300 650 305 C850 310 1050 260 1190 140 L1190 310 L1200 310 L1200 310 L0 310 Z" fill="var(--mist)"/>
    <path d="M0 262 C200 195 340 185 520 225 C620 245 640 245 700 240" fill="none" stroke="var(--white)" stroke-width="8"/>
  </svg>
  <h1 class="hero-title">Building concrete pools &amp; Renovate concrete pools</h1>
  <div class="hero-cta">Get Startes</div>
</section>

<section class="band abs" style="top:398px;height:517px">
  <h2 class="dream-title">Choose Your Dream Pool</h2>
  <p class="dream-sub">With various innovations and variations as well as models of each flagship product that are up-to-date, luxurious and elegant, able to provide comfort.</p>
  <div class="cols" style="top:113px">
    <div class="col">
      <div class="photo" role="img" aria-label="Modern house with lit pool at dusk" style="width:278px;height:222px;background:linear-gradient(160deg,#2a47d6,#3b6a3a 55%,#8fe0d8)"></div>
      <div class="style-label">Modern</div>
      <p class="copy">Lorem ipsum dolor sit amet, consectetur adipiscing elit, sed do eiusmod tempor incididunt ut labore et dolore magna aliqua.</p>
      <div class="btn" style="margin-top:24px">Explore more</div>
    </div>
    <div class="col">
      <div class="photo" role="img" aria-label="Rectangular tiled pool with umbrella and garden" style="width:278px;height:222px;background:linear-gradient(180deg,#4d6b3c,#7d9a8a 40%,#5b9dd6 70%,#6e5a4a)"></div>
      <div class="style-label">Geometric</div>
      <p class="copy">Lorem ipsum dolor sit amet, consectetur adipiscing elit, sed do eiusmod tempor incididunt ut labore et dolore magna aliqua.</p>
      <div class="btn" style="margin-top:24px">Explore more</div>
    </div>
    <div class="col">
      <div class="photo" role="img" aria-label="Free-form pool with wooden deck and fountain" style="width:278px;height:222px;background:linear-gradient(180deg,#8a5a3a,#c8845a 35%,#3aa8f0 55%,#2f8ce8)"></div>
      <div class="style-label">Free Form</div>
      <p class="copy">Lorem ipsum dolor sit amet, consectetur adipiscing elit, sed do eiusmod tempor incididunt ut labore et dolore magna aliqua.</p>
      <div class="btn" style="margin-top:24px">Explore more</div>
    </div>
  </div>
</section>

<section class="band abs" style="top:945px;height:445px">
  <h2 class="section-title" style="top:30px">Our Service</h2>
  <p class="section-sub" style="top:75px">Services provided by experts in their fields who are ready to serve you</p>
  <div class="cols" style="top:115px">
    <div class="col">
      <div class="icon-box"><svg width="102" height="88" viewBox="0 0 102 88"><ellipse cx="51" cy="44" rx="49" ry="42" fill="none" stroke="var(--navy)" stroke-width="2.5"/><path d="M40 58 46 40 58 32 64 38 56 50Z" fill="var(--navy)"/><path d="M58 32 62 26 70 34 64 38Z" fill="var(--navy)"/></svg></div>
      <h3 class="service-name">Design</h3>
      <p class="copy">Lorem ipsum dolor sit amet, consectetur adipiscing elit, sed do eiusmod tempor incididunt ut labore et dolore magna aliqua.</p>
      <div class="btn" style="margin-top:24px">Explore more</div>
    </div>
    <div class="col">
      <div class="icon-box"><svg width="102" height="88" viewBox="0 0 102 88"><ellipse cx="51" cy="44" rx="49" ry="42" fill="none" stroke="var(--navy)" stroke-width="2.5"/><circle cx="46" cy="32" r="5" fill="var(--navy)"/><path d="M36 56 42 40h8l6 8-4 3-4-5-3 10z" fill="var(--navy)"/><path d="M52 58 62 46 70 58z" fill="var(--navy)"/></svg></div>
      <h3 class="service-name">Construction</h3>
      <p class="copy">Lorem ipsum dolor sit amet, consectetur adipiscing elit, sed do eiusmod tempor incididunt ut labore et dolore magna aliqua.</p>
      <div class="btn" style="margin-top:24px">Explore more</div>
    </div>
    <div class="col">
      <div class="icon-box"><svg width="102" height="88" viewBox="0 0 102 88"><ellipse cx="51" cy="44" rx="49" ry="42" fill="none" stroke="var(--navy)" stroke-width="2.5"/><rect x="39" y="32" width="24" height="24" rx="3" fill="var(--navy)"/><rect x="45" y="38" width="12" height="12" fill="var(--white)"/><path d="M44 28v4M51 28v4M58 28v4M44 56v4M51 56v4M58 56v4M35 37h4M35 44h4M35 51h4M63 37h4M63 44h4M63 51h4" stroke="var(--navy)" stroke-width="2.5"/></svg></div>
      <h3 class="service-name">Excelence</h3>
      <p class="copy">Lorem ipsum dolor sit amet, consectetur adipiscing elit, sed do eiusmod tempor incididunt ut labore et dolore magna aliqua.</p>
      <div class="btn" style="margin-top:24px">Explore more</div>
    </div>
  </div>
</section>

<section class="band abs" style="top:1428px;height:527px">
  <h2 class="section-title" style="top:19px;color:var(--ink);font-size:30px">Our Projects</h2>
  <div class="cols" style="top:66px">
    <div class="col">
      <div class="photo" role="img" aria-label="Modern multi-storey villa with pool at twilight" style="width:260px;height:300px;background:linear-gradient(180deg,#5a63c8,#2a2440 55%,#1a1a2a)"></div>
      <h3 class="project-name">Description</h3>
      <p class="copy">Lorem ipsum dolor sit amet, consectetur adipiscing elit, sed do eiusmod tempor incididunt ut labore et dolore magna aliqua.</p>
      <div class="btn" style="margin-top:24px">Explore more</div>
    </div>
    <div class="col">
      <div class="photo" role="img" aria-label="Infinity pool deck with loungers overlooking the sea" style="width:276px;height:300px;background:linear-gradient(180deg,#5ab8e8,#a8d8e8 30%,#3a8a4a 50%,#b04a3a 80%)"></div>
      <h3 class="project-name">Description</h3>
      <p class="copy">Lorem ipsum dolor sit amet, consectetur adipiscing elit, sed do eiusmod tempor incididunt ut labore et dolore magna aliqua.</p>
      <div class="btn" style="margin-top:24px">Explore more</div>
    </div>
    <div class="col">
      <div class="photo" role="img" aria-label="Tropical villa with long turquoise pool and palms" style="width:346px;height:300px;background:linear-gradient(180deg,#3a8ae0,#4a7a3a 35%,#e8e8e0 55%,#3ad0d8 75%,#a8b8b8)"></div>
      <h3 class="project-name">Description</h3>
      <p class="copy">Lorem ipsum dolor sit amet, consectetur adipiscing elit, sed do eiusmod tempor incididunt ut labore et dolore magna aliqua.</p>
      <div class="btn" style="margin-top:24px">Explore more</div>
    </div>
  </div>
</section>

<div class="band abs" style="top:2032px;height:368px"></div>
<div class="contact-brand abs">
  <div class="brand"><span class="brand-mark" style="width:66px;height:66px"></span><div class="brand-text"><span class="brand-name" style="font-size:48px">Aquavell</span><span class="brand-tag" style="font-size:11px">THE POOL SERVICE COMPANY</span></div></div>
</div>
<form class="contact-form abs">
  <span class="field-label">Last Name</span>
  <div class="field">Your last name..</div>
  <span class="field-label">Country</span>
  <div class="field select">Australia <svg width="10" height="6" viewBox="0 0 10 6"><path d="M1 1 5 5 9 1" fill="none" stroke="#111" stroke-width="1.8"/></svg></div>
  <span class="field-label">Subject</span>
  <div class="field area">Write something..</div>
  <div class="submit">Submit</div>
</form>

<footer class="site-footer abs">
  <div class="brand"><span class="brand-mark"></span><div class="brand-text"><span class="brand-name">Aquavell</span><span class="brand-tag" style="font-size:9px">THE POOL SERVICE COMPANY</span></div></div>
  <div class="footer-col" style="left:524px">
    <h4>Address</h4>
    <div class="line"><svg width="16" height="16" viewBox="0 0 24 24"><path fill="#fff" d="M6.6 10.8a15 15 0 0 0 6.6 6.6l2.2-2.2a1 1 0 0 1 1-.25 11 11 0 0 0 3.6.6 1 1 0 0 1 1 1V20a1 1 0 0 1-1 1A17 17 0 0 1 3 4a1 1 0 0 1 1-1h3.5a1 1 0 0 1 1 1c0 1.25.2 2.45.6 3.6a1 1 0 0 1-.25 1z"/></svg>000-000-0000</div>
    <div class="line"><svg width="16" height="12" viewBox="0 0 16 12"><rect width="16" height="12" fill="#fff"/><path d="M0 0 8 7 16 0" fill="none" stroke="var(--footer)" stroke-width="1.5"/></svg>example@aquavell.com</div>
    <div>detail address, DTAIL ADDRESS</div>
  </div>
  <div class="footer-col" style="left:791px">
    <h4>Menu</h4>
    <div>Home</div><div>About Us</div><div>Our Services</div><div>Contact Us</div>
  </div>
  <div class="socials" aria-label="Social links"><span></span><span></span><span></span></div>
  <p class="copyright">AQUAVELL | 2023 | All Rights Reserved</p>
</footer>

</div>
</body>
</html>
```